Church Bulletin Ad (see attached sample)

Create a New Church Bulletin Ad. I have attached some samples of what we would like to have in the ad. (1) Marrowfield Realty Thorne Logo (2) Headshot (3) Lena Vasko & Greta Vasko, Real Estate Team (4) Phone number (5) Email address (6) St Aldwin Parishioners for over 40 Years. We would like for the ad to be clean and modern. NO OTHER IMAGES besides headshots and Marrowfield Realty Thorne Logo.

Target Market(s)

Church community

Industry/Entity Type

Real Estate

Font styles to use
Sans Serif
Other font styles liked:
• Modern Font

Colors
0054AA
0677BA
7BADD7
CADEEF
E8F1F8

Requirements
Must have
• Marrowfield Realty Thorne Logo; Headshot; Ad size is 4.5"x1.62"

```html
<!DOCTYPE html>
<html lang="en">
<head>
<meta charset="utf-8">
<title>Vasko Real Estate Team – Bulletin Ad</title>
<link rel="stylesheet" href="https://fonts.googleapis.com/css2?family=Montserrat:wght@500;600;800&family=Marcellus&display=swap">
<style>
  :root {
    --navy: #0b2b56;
    --accent: #0a9bc8;
    --white: #ffffff;
    --photo-a: #d9c3b3;
    --photo-b: #6b4a3a;
    --photo-c: #ece7e2;
    --photo-d: #c9a899;
    --photo-e: #3a3030;
  }
  * { margin: 0; padding: 0; box-sizing: border-box; }
  html, body { width: 1200px; height: 432px; overflow: hidden; background: var(--navy); }
  .ad {
    position: relative; width: 1200px; height: 432px; overflow: hidden;
    background: var(--navy); color: var(--white);
    font-family: "Montserrat", sans-serif;
  }
  .ad__shapes { position: absolute; inset: 0; }
  .tagline {
    position: absolute; left: 32px; top: 30px; list-style: none;
    font-weight: 800; font-size: 39px; line-height: 45px; letter-spacing: 0.3px;
  }
  .tagline__word--highlight {
    display: inline-block; background: var(--accent);
    padding: 0 11px 0 2px; margin-left: -2px; line-height: 40px;
  }
  .contact {
    position: absolute; left: 32px; top: 207px; list-style: none;
    font-weight: 500; font-size: 23.5px; line-height: 25px;
  }
  .contact li::before {
    content: ""; display: inline-block; width: 7px; height: 7px; border-radius: 50%;
    background: var(--white); margin-right: 5px; vertical-align: middle;
  }
  .parish {
    position: absolute; left: 32px; top: 323px;
    font-weight: 600; font-size: 23.5px; line-height: 26px;
  }
  .parish__years { color: var(--accent); }
  .brand {
    position: absolute; left: 339px; top: 292px; width: 127px; height: 117px;
    border: 3px solid var(--white);
    display: flex; align-items: center; justify-content: center; text-align: center;
    font-weight: 600; font-size: 15px; line-height: 19px; padding: 8px;
  }
  .name {
    position: absolute; font-family: "Marcellus", serif; color: var(--white);
    text-align: center; white-space: nowrap; line-height: 1.15;
  }
  .name--lena { left: 467px; width: 345px; top: 9px; font-size: 41px; }
  .name--greta { left: 838px; width: 344px; top: 377px; font-size: 42px; }
  .team-label {
    position: absolute; left: 467px; width: 345px; top: 377px; text-align: center;
    font-family: "Marcellus", serif; font-size: 34px; line-height: 1.15;
  }
</style>
</head>
<body>
<main class="ad">
  <svg class="ad__shapes" width="1200" height="432" viewBox="0 0 1200 432">
    <defs>
      <linearGradient id="headshot-lena" x1="0" y1="0" x2="0" y2="1">
        <stop offset="0" stop-color="var(--photo-b)"/>
        <stop offset="0.55" stop-color="var(--photo-a)"/>
        <stop offset="1" stop-color="var(--photo-b)"/>
      </linearGradient>
      <linearGradient id="headshot-greta" x1="0" y1="0" x2="0" y2="1">
        <stop offset="0" stop-color="var(--photo-c)"/>
        <stop offset="0.6" stop-color="var(--photo-d)"/>
        <stop offset="1" stop-color="var(--photo-e)"/>
      </linearGradient>
    </defs>
    <path class="panel panel--lena" d="M467 0 H811 V194 A172 172 0 0 1 467 194 Z" fill="var(--accent)"/>
    <path class="panel panel--greta" d="M838 432 V236 A172 172 0 0 1 1182 236 V432 Z" fill="var(--accent)"/>
    <circle cx="639" cy="213" r="145" fill="var(--white)"/>
    <circle cx="639" cy="213" r="136" fill="url(#headshot-lena)" role="img" aria-label="Headshot of Lena Vasko"/>
    <circle cx="1011" cy="221" r="145" fill="var(--white)"/>
    <circle cx="1011" cy="221" r="136" fill="url(#headshot-greta)" role="img" aria-label="Headshot of Greta Vasko"/>
  </svg>

  <ul class="tagline">
    <li>ENERGY</li>
    <li><span class="tagline__word--highlight">EXCELLENCE</span></li>
    <li>EXPERIENCE</li>
  </ul>

  <ul class="contact">
    <li>(206) 555-0148</li>
    <li>vaskoteam@marrowthorne.com</li>
  </ul>

  <p class="parish">St Aldwin Parishioners<br>for over <span class="parish__years">40 Years</span></p>

  <div class="brand">Marrowfield Realty Thorne</div>

  <p class="name name--lena">Lena Vasko</p>
  <p class="team-label">Real Estate Team</p>
  <p class="name name--greta">Greta Vasko</p>
</main>
</body>
</html>
```